SipNOW Business Cards

Hi designers!

Here's some background on our start-up and this project:

SipNOW is a website that will allow users to order alcohol from nearby liquor stores and have it delivered to their homes in minutes. We are really excited to work on creating the best online, alcohol purchasing experience for the users.

So why SipNOW? We like to think of ourselves as that great friend who will get alcohol for you because he happens to have a car. We help you drink in with your friends, family, or guests. Our site will target students and young professionals (of drinking age) who are comfortable buying things online or through apps. We don't see this service as a luxury, VIP, or niche service in the least; instead, we think of us as a relaxed, service-driven start-up that believes in simple design and transparent .

Now, we want a business card that incorporates our newly acquired logo design and some complimenting colors and fonts. Feel free to do it single or double sided, although I'm a sucker for double...

If you happen to have any questions, want to throw some ideas around, or just want some feedback- email me at marco@sipnow.example.

Marco Tessin
Founder

Industry/Entity Type

Business

Requirements
Must have
• Name, Position, Email, Cell-phone

No address, no fax, no land-line.

```html
<!DOCTYPE html>
<html lang="en">
<head>
<meta charset="utf-8">
<title>SipNOW Business Cards</title>
<link href="https://fonts.googleapis.com/css2?family=Open+Sans:wght@400;800&family=Arimo&display=swap" rel="stylesheet">
<style>
  :root {
    --ink: #000000;
    --paper: #ffffff;
    --amber: #f7c415;
    --frame: #222222;
  }
  html, body {
    margin: 0;
    padding: 0;
    width: 927px;
    height: 1200px;
    overflow: hidden;
    background: var(--paper);
  }
  .sheet {
    position: relative;
    width: 927px;
    height: 1200px;
    font-family: "Open Sans", Arial, sans-serif;
    color: var(--ink);
  }
  .card {
    position: absolute;
    box-sizing: border-box;
    overflow: hidden;
  }
  .wordmark {
    position: absolute;
    font-weight: 800;
    line-height: 1;
    white-space: nowrap;
    letter-spacing: -1px;
  }
  .person, .contact {
    position: absolute;
    line-height: 1.35;
    white-space: nowrap;
  }
  .person .name { display: block; }
  .person .role { display: block; color: var(--amber); }
  .contact { text-align: right; }
  .contact span { display: block; }

  /* Front option 1 */
  .front-one {
    left: 120px; top: 76px; width: 372px; height: 213px;
    border: 1.5px solid var(--frame);
    background: var(--paper);
  }
  .front-one .wordmark { left: 38px; top: 34px; font-size: 70px; color: var(--ink); }
  .front-one .person { left: 39px; top: 132px; font-size: 16.5px; }
  .front-one .contact { right: 38px; top: 132px; font-size: 14.5px; }
  .front-one .phone { color: var(--amber); }

  /* Front option 2 */
  .front-two {
    left: 121px; top: 373px; width: 371px; height: 211px;
    background: var(--paper);
  }
  .front-two .bands { position: absolute; inset: 0; }
  .front-two .wordmark { left: 0; right: 0; text-align: center; top: 80px; font-size: 44px; color: var(--ink); }
  .front-two .person { left: 19px; top: 10px; font-size: 16.5px; color: var(--paper); }
  .front-two .contact { right: 26px; top: 152px; font-size: 14.5px; color: var(--paper); }

  /* Optional back */
  .back {
    left: 117px; top: 700px; width: 371px; height: 212px;
    background: linear-gradient(to right, var(--amber) 0, var(--amber) 253px, var(--ink) 253px);
  }
  .back .wordmark { left: 0; right: 0; text-align: center; top: 70px; font-size: 66px; color: var(--paper); }

  .caption {
    position: absolute;
    left: 593px;
    font-family: "Arimo", Arial, sans-serif;
    font-size: 17px;
    color: var(--ink);
    white-space: nowrap;
  }
</style>
</head>
<body>
<main class="sheet">

  <section class="card front-one" aria-label="Front option 1">
    <div class="wordmark">SipNOW</div>
    <p class="person" style="margin:0"><span class="name">Marco Tessin</span><span class="role">Founder</span></p>
    <p class="contact" style="margin:0"><span class="phone">(555) 014-23876</span><span class="email">email@sipnow.example</span></p>
  </section>
  <p class="caption" style="top:148px;margin:0">Front option 1</p>

  <section class="card front-two" aria-label="Front option 2">
    <svg class="bands" width="371" height="211" viewBox="0 0 371 211" aria-hidden="true">
      <polygon points="0,0 222,0 0,115" fill="var(--ink)"/>
      <polygon points="371,70 371,211 99,211" fill="var(--ink)"/>
    </svg>
    <div class="wordmark">SipNOW</div>
    <p class="person" style="margin:0"><span class="name">Marco Tessin</span><span class="role">Founder</span></p>
    <p class="contact" style="margin:0"><span>(555) 014-23876</span><span>email@sipnow.example</span></p>
  </section>
  <p class="caption" style="top:413px;margin:0">Front option 2</p>

  <section class="card back" aria-label="Optional back">
    <div class="wordmark">SipNOW</div>
  </section>
  <p class="caption" style="top:776px;margin:0">Optional Back</p>

</main>
</body>
</html>
```